Talvor GmbH business card

We Talvor GmbH based in Switzerland are looking for a business card design. The Fresh Jung, appealing to customers of all kinds. We already have a logo to upload but still a business card. Details: Talvor GmbH Address: Lindenweg 14b in 9476 Brugwil. Tel: 41 79 462 37 18, web: Talvor.ch, E-mail: info@Talvor.ch Facebook: Talvor GmbH. I am the Managing Director: Luka Petrovac. On reverse: Title: Transporter and bus rental Gross: Without deposit Super prices
Contact Information for Business Card
Siehe Projektbeschreibung
Requirements
Should not have
- Other pictures

```html
<!DOCTYPE html>
<html lang="de">
<head>
<meta charset="utf-8">
<title>Talvor GmbH – Visitenkarte</title>
<link href="https://fonts.googleapis.com/css2?family=Open+Sans:wght@400;600;700&display=swap" rel="stylesheet">
<style>
  :root {
    --bg: #1c1c1e;
    --paper: #ffffff;
    --ink: #222222;
    --navy: #2b2f86;
    --brand-blue: #3035a8;
    --band: #262a7c;
    --charcoal: #232325;
    --white: #ffffff;
  }
  * { box-sizing: border-box; margin: 0; padding: 0; }
  html, body { width: 1200px; height: 900px; overflow: hidden; }
  body { background: var(--bg); font-family: "Open Sans", Arial, sans-serif; position: relative; }

  .card { position: absolute; width: 660px; height: 380px; border-radius: 34px; overflow: hidden; }

  /* Front */
  .card-front { left: 90px; top: 50px; background: var(--paper); }
  .front-brand { position: absolute; left: 150px; top: 140px; display: flex; align-items: center; gap: 20px; }
  .brand-mark { width: 40px; height: 40px; background: var(--navy); }
  .front-brand .brand-name { font-size: 72px; font-weight: 700; color: var(--navy); letter-spacing: 3px; }
  .tagline { position: absolute; right: 40px; bottom: 44px; font-size: 15px; color: var(--ink); letter-spacing: .5px; }
  .edge-tab { position: absolute; right: 0; bottom: 64px; width: 26px; height: 12px; background: var(--ink); }

  /* Back */
  .card-back { left: 450px; top: 470px; background: var(--charcoal); }
  .blue-panel { position: absolute; left: 330px; top: 0; width: 330px; height: 100%; background: linear-gradient(160deg, #3a3fbb, var(--brand-blue) 60%, #2a2e9a); }
  .address-band { position: absolute; left: 300px; top: 52px; width: 360px; height: 46px; background: var(--band); display: flex; align-items: center; gap: 10px; padding-left: 18px; color: var(--white); font-size: 15px; letter-spacing: .3px; }
  .address-band svg { flex: none; }
  .name-block { position: absolute; left: 0; top: 98px; display: flex; gap: 16px; align-items: flex-start; }
  .name-accent { width: 22px; height: 52px; background: var(--brand-blue); }
  .person-name { color: var(--white); font-size: 26px; font-weight: 600; letter-spacing: 1px; line-height: 1.1; }
  .person-role { color: var(--white); font-size: 12.5px; letter-spacing: .4px; margin-top: 4px; }
  .contact-list { position: absolute; left: 40px; bottom: 40px; list-style: none; color: var(--white); font-size: 16px; letter-spacing: .6px; }
  .contact-list li { display: flex; align-items: center; gap: 14px; height: 30px; }
  .contact-list svg { flex: none; }
  .back-brand { position: absolute; left: 370px; top: 220px; display: flex; align-items: center; gap: 14px; }
  .back-brand .brand-mark { width: 28px; height: 28px; background: var(--white); }
  .back-brand .brand-name { font-size: 46px; font-weight: 700; color: var(--white); letter-spacing: 2px; }
</style>
</head>
<body>
  <section class="card card-front" aria-label="Vorderseite">
    <div class="front-brand">
      <span class="brand-mark"></span>
      <span class="brand-name">TALVOR</span>
    </div>
    <p class="tagline">Transporter und Bus vermietung</p>
    <span class="edge-tab"></span>
  </section>

  <section class="card card-back" aria-label="Rückseite">
    <div class="blue-panel"></div>
    <div class="address-band">
      <svg width="16" height="20" viewBox="0 0 16 20" fill="none" stroke="#fff" stroke-width="1.4"><path d="M8 19s6-6.5 6-11A6 6 0 0 0 2 8c0 4.5 6 11 6 11z"/><circle cx="8" cy="8" r="2.2"/></svg>
      <span>Lindenweg 14b in 9476 Brugwil</span>
    </div>
    <div class="name-block">
      <span class="name-accent"></span>
      <div>
        <h1 class="person-name">LUKA PETROVAC</h1>
        <p class="person-role">ICH BIN DER GESCHÄFTSFÜHRER</p>
      </div>
    </div>
    <ul class="contact-list">
      <li><svg width="18" height="18" viewBox="0 0 18 18" fill="none" stroke="#fff" stroke-width="1.3"><path d="M4 2l3 3-2 2a10 10 0 0 0 6 6l2-2 3 3-2 2C8 16 2 10 2 4z"/></svg>+41 79 462 37 18</li>
      <li><svg width="18" height="14" viewBox="0 0 18 14" fill="none" stroke="#fff" stroke-width="1.3"><rect x="1" y="1" width="16" height="12"/><path d="M1 1l8 7 8-7"/></svg>info@Talvor.ch</li>
      <li><svg width="18" height="18" viewBox="0 0 18 18" fill="none" stroke="#fff" stroke-width="1.2"><circle cx="9" cy="9" r="8"/><ellipse cx="9" cy="9" rx="3.5" ry="8"/><path d="M1 9h16M2.5 5h13M2.5 13h13"/></svg>www.Talvor.ch</li>
      <li><svg width="18" height="18" viewBox="0 0 18 18" fill="none" stroke="#fff" stroke-width="1.3"><path d="M11 2h-2a3 3 0 0 0-3 3v2H4v3h2v7h3v-7h2.5l.5-3H9V5.5c0-.5.3-.8.8-.8H11z"/></svg>Talvor GmbH</li>
    </ul>
    <div class="back-brand">
      <span class="brand-mark"></span>
      <span class="brand-name">TALVOR</span>
    </div>
  </section>
</body>
</html>
```